Product Designer Business Card

Small product design, engineering and prototyping firm in need of a clean, professional business card design. To support our 3D design and drawing services, we offer 3D printing, molding, and casting of plastics, silicones, resins, etc. Our logo can still be modified/changed if necessary. The red/orange color is preferred, but may be substituted with blue or green, potentially. Either way, the colour of the logo should be match/compliment colors used throughout the design. One thought is to have the logo/contact info on one side, with the other side describing services offered, like with a small icon of 3D printer, molding, casting, and computer with a 3D model on-screen.
Industry/Entity Type
Mechanical Engineering
Contact Information for Business Card
Company: Halvick Design
Phone: 613-582-4179
Email: myles@halvickdesign.ca

```html
<!DOCTYPE html>
<html lang="en">
<head>
<meta charset="utf-8">
<title>Halvick Design — Business Card</title>
<link rel="stylesheet" href="https://fonts.googleapis.com/css2?family=Jost:wght@400;600;700&family=Lato:wght@400&display=swap">
<style>
  :root {
    --page: #d9d9d9;
    --card-dark: #191919;
    --card-light: #ffffff;
    --red-bright: #ff2416;
    --red-mid: #d30000;
    --red-deep: #9a0000;
    --brand-dark: #7a1006;
    --text-light: #ffffff;
  }
  html, body {
    margin: 0;
    padding: 0;
    width: 1200px;
    height: 1200px;
    overflow: hidden;
    background: var(--page);
  }
  .canvas {
    position: relative;
    width: 1200px;
    height: 1200px;
  }
  .card {
    position: absolute;
    left: 240px;
    width: 725px;
    height: 416px;
    display: block;
  }
  .card--front { top: 129px; }
  .card--back { top: 655px; }
  .wordmark {
    font-family: "Jost", sans-serif;
    font-weight: 600;
  }
  .headline {
    font-family: "Jost", sans-serif;
    font-size: 48px;
    letter-spacing: 1px;
  }
  .headline__strong { font-weight: 700; }
  .headline__light { font-weight: 400; }
  .contact {
    font-family: "Lato", sans-serif;
    font-size: 29px;
    fill: var(--text-light);
  }
</style>
</head>
<body>
<main class="canvas">

  <!-- Front side -->
  <svg class="card card--front" viewBox="0 0 1168 670" role="img" aria-label="Halvick Design business card, front">
    <defs>
      <linearGradient id="front-band" x1="0" y1="0" x2="1" y2="0.6">
        <stop offset="0" stop-color="var(--red-deep)"/>
        <stop offset="0.35" stop-color="var(--red-mid)"/>
        <stop offset="0.6" stop-color="var(--red-bright)"/>
        <stop offset="1" stop-color="var(--red-deep)"/>
      </linearGradient>
      <linearGradient id="front-shade" x1="0" y1="0" x2="0" y2="1">
        <stop offset="0" stop-color="#000"/>
        <stop offset="1" stop-color="#191919"/>
      </linearGradient>
    </defs>
    <rect class="card__base" width="1168" height="670" fill="var(--card-dark)"/>
    <rect class="card__shade" x="740" y="489" width="428" height="70" fill="url(#front-shade)"/>
    <polygon class="card__band" points="87,0 209,0 134,134 337,489 759,489 727,548 249,548 12,134" fill="url(#front-band)"/>
    <polygon class="card__panel" points="209,0 1168,0 1168,489 337,489 134,134" fill="var(--card-light)"/>
    <circle cx="520" cy="192" r="18" fill="var(--red-mid)"/>
    <text class="wordmark" x="700" y="212" text-anchor="middle" font-size="64" fill="var(--brand-dark)">Halvick</text>
    <text class="wordmark" x="680" y="328" text-anchor="middle" font-size="46" letter-spacing="28" fill="var(--brand-dark)">Design</text>
  </svg>

  <!-- Back side -->
  <svg class="card card--back" viewBox="0 0 1168 670" role="img" aria-label="Halvick Design business card, back with contact details">
    <defs>
      <linearGradient id="back-band-top" x1="0" y1="1" x2="1" y2="0">
        <stop offset="0" stop-color="var(--red-deep)"/>
        <stop offset="0.55" stop-color="var(--red-bright)"/>
        <stop offset="0.8" stop-color="var(--red-mid)"/>
        <stop offset="1" stop-color="var(--red-bright)"/>
      </linearGradient>
      <linearGradient id="back-band-low" x1="0" y1="1" x2="1" y2="0">
        <stop offset="0" stop-color="var(--red-deep)"/>
        <stop offset="0.4" stop-color="var(--red-mid)"/>
        <stop offset="0.55" stop-color="var(--red-bright)"/>
        <stop offset="1" stop-color="var(--red-deep)"/>
      </linearGradient>
      <linearGradient id="back-shade" x1="0" y1="0" x2="0" y2="1">
        <stop offset="0" stop-color="#000"/>
        <stop offset="1" stop-color="#191919"/>
      </linearGradient>
    </defs>
    <rect class="card__base" width="1168" height="670" fill="var(--card-dark)"/>
    <rect class="card__shade" x="0" y="259" width="120" height="70" fill="url(#back-shade)"/>
    <rect class="card__shade" x="1000" y="282" width="168" height="51" fill="#000"/>
    <polygon class="card__band" points="587,0 693,0 516,310 105,310 77,259 440,259" fill="url(#back-band-top)"/>
    <polygon class="card__band" points="601,282 1011,282 1040,333 676,333 501,639 518,670 414,670 396,639" fill="url(#back-band-low)"/>

    <text class="headline" x="93" y="153" fill="var(--red-bright)">
      <tspan class="headline__strong">HALVICK</tspan> <tspan class="headline__light">DESIGN</tspan>
    </text>
    <rect class="headline__rule" x="93" y="172" width="326" height="3" fill="var(--text-light)"/>
    <rect class="headline__accent" x="93" y="170" width="57" height="7" fill="var(--red-mid)"/>

    <circle cx="782" cy="120" r="16" fill="var(--text-light)"/>
    <text class="wordmark" x="920" y="140" text-anchor="middle" font-size="58" fill="var(--text-light)">Halvick</text>
    <text class="wordmark" x="900" y="212" text-anchor="middle" font-size="32" letter-spacing="20" fill="var(--text-light)">Design</text>

    <g class="contact-row">
      <path class="icon icon--phone" fill="var(--text-light)" d="M546 452c3-3 7-3 9 0l5 7c2 3 1 6-1 8l-3 2c2 5 6 9 11 12l2-3c2-2 5-3 8-1l6 4c3 2 3 6 0 9l-3 3c-4 3-10 3-16-1-8-5-15-13-19-22-2-6-2-11 1-15z"/>
      <text class="contact" x="609" y="475">613-582-4179</text>
    </g>
    <g class="contact-row">
      <g class="icon icon--mail">
        <rect x="508" y="509" width="32" height="21" fill="var(--text-light)"/>
        <polyline points="508,509 524,522 540,509" fill="none" stroke="var(--card-dark)" stroke-width="2"/>
        <polyline points="508,530 519,520 M540,530 529,520" fill="none" stroke="var(--card-dark)" stroke-width="2"/>
      </g>
      <text class="contact" x="573" y="529">myles@halvickdesign.ca</text>
    </g>
  </svg>

</main>
</body>
</html>
```